Esport Center Food Menu

We need a cool food menu designed for our Esports facility, a place for people to play all the latest esport games and we serve food and drinks. It will be put on our website, printed and put on quality paper the size of printer paper and will be put on a television screen. We would like the colors to go well with our logo. Color scheme Red/Black/White/Light Gray/Dark Gray. Attached is the example we came up with, it has to look cooler than this! Our font is http://www.typorell.net/kovanteri.font

Industry/Entity Type

Games

Requirements
Must have
• Our logo in it, match our color scheme
Nice to have
• Our font is http://www.typorell.net/kovanteri.font
• We are having different beers that will be changed monthly. If there is a cool way to make these beers stand out, that would be nice to have.

```html
<!DOCTYPE html>
<html lang="en">
<head>
<meta charset="utf-8">
<title>Pixel Forge Cafe Menu</title>
<link rel="stylesheet" href="https://fonts.googleapis.com/css2?family=Audiowide&display=swap">
<style>
  :root {
    --red: #a30d0d;
    --red-dark: #6e0707;
    --red-fold: #4a0404;
    --black: #050505;
    --white: #ffffff;
    --light-gray: #d9d9d9;
    --wood: #5a3a22;
    --wood-dark: #2e1d12;
  }
  * { margin: 0; padding: 0; box-sizing: border-box; }
  html, body { width: 826px; height: 1200px; overflow: hidden; background: var(--light-gray); }
  .menu {
    position: relative; width: 826px; height: 1200px; overflow: hidden;
    font-family: "Audiowide", sans-serif; color: var(--white); text-transform: uppercase;
  }
  .table-photo {
    position: absolute; inset: 0;
    background: radial-gradient(ellipse at 20% 60%, #8a6a44 0%, var(--wood) 45%, var(--wood-dark) 100%);
  }
  .board {
    position: absolute; left: 46px; right: 58px; top: 36px; bottom: 26px;
    background: var(--black);
    box-shadow: 0 0 18px 10px rgba(0,0,0,0.85);
  }
  .brand {
    position: absolute; left: 0; right: 0; top: 112px; text-align: center;
    font-size: 50px; color: var(--red); letter-spacing: 2px;
  }
  .cafe-name {
    position: absolute; left: 0; right: 0; top: 186px; text-align: center;
    font-size: 36px; letter-spacing: 3px;
  }
  .rule { position: absolute; left: 253px; width: 320px; height: 2px; background: var(--white); }
  .ribbon { position: absolute; left: 183px; width: 460px; height: 46px; }
  .ribbon-label {
    position: absolute; left: 0; right: 0; text-align: center;
    font-size: 25px; letter-spacing: 1px; line-height: 30px;
  }
  .item {
    position: absolute; left: 0; right: 0; text-align: center;
    font-size: 19px; letter-spacing: 2px; line-height: 22px;
  }
  .note { position: absolute; left: 0; right: 0; text-align: center; font-size: 11px; letter-spacing: 2px; }
  .wide-note { position: absolute; left: 0; right: 0; text-align: center; font-size: 16px; letter-spacing: 4px; }
</style>
</head>
<body>
<main class="menu">
  <div class="table-photo" role="img" aria-label="Overhead photo of a wooden table with plates of food, drinks and chopsticks"></div>
  <div class="board"></div>

  <div class="brand">Pixel Forge</div>
  <div class="cafe-name">Pixel Forge Cafe</div>

  <!-- Panini -->
  <div class="rule" style="top:252px"></div>
  <svg class="ribbon" style="top:266px" viewBox="0 0 460 46" aria-hidden="true">
    <polygon points="0,14 40,14 40,46 0,46 12,30" fill="var(--red-dark)"/>
    <polygon points="460,14 420,14 420,46 460,46 448,30" fill="var(--red-dark)"/>
    <polygon points="28,40 40,46 40,40" fill="var(--red-fold)"/>
    <polygon points="432,40 420,46 420,40" fill="var(--red-fold)"/>
    <rect x="28" y="2" width="404" height="38" fill="var(--red)"/>
  </svg>
  <div class="ribbon-label" style="top:270px">Panini</div>
  <div class="rule" style="top:297px"></div>
  <div class="item" style="top:322px">Buffalo Chicken</div>
  <div class="item" style="top:347px">Ham &amp; Cheese</div>
  <div class="item" style="top:371px">BBQ Chicken</div>
  <div class="item" style="top:395px">Turkey Swiss</div>

  <!-- Air fried -->
  <div class="rule" style="top:442px"></div>
  <svg class="ribbon" style="top:455px" viewBox="0 0 460 46" aria-hidden="true">
    <polygon points="0,14 40,14 40,46 0,46 12,30" fill="var(--red-dark)"/>
    <polygon points="460,14 420,14 420,46 460,46 448,30" fill="var(--red-dark)"/>
    <polygon points="28,40 40,46 40,40" fill="var(--red-fold)"/>
    <polygon points="432,40 420,46 420,40" fill="var(--red-fold)"/>
    <rect x="28" y="2" width="404" height="38" fill="var(--red)"/>
  </svg>
  <div class="ribbon-label" style="top:459px">Air Fried</div>
  <div class="rule" style="top:486px"></div>
  <div class="note" style="top:514px">(Full or half orders)</div>
  <div class="item" style="top:533px">Chicken Tenders</div>
  <div class="item" style="top:557px">Fried Pickles</div>
  <div class="item" style="top:582px">Fries</div>
  <div class="item" style="top:605px">Loaded Fries</div>
  <div class="note" style="top:628px">(Buffalo or Nacho)</div>
  <div class="wide-note" style="top:646px">Assorted snacks also available</div>

  <!-- Drinks -->
  <div class="rule" style="top:695px"></div>
  <svg class="ribbon" style="top:708px" viewBox="0 0 460 46" aria-hidden="true">
    <polygon points="0,14 40,14 40,46 0,46 12,30" fill="var(--red-dark)"/>
    <polygon points="460,14 420,14 420,46 460,46 448,30" fill="var(--red-dark)"/>
    <polygon points="28,40 40,46 40,40" fill="var(--red-fold)"/>
    <polygon points="432,40 420,46 420,40" fill="var(--red-fold)"/>
    <rect x="28" y="2" width="404" height="38" fill="var(--red)"/>
  </svg>
  <div class="ribbon-label" style="top:712px">Drinks</div>
  <div class="rule" style="top:739px"></div>
  <div class="item" style="top:766px">Volt Energy Drink</div>
  <div class="item" style="top:791px">Pixel Forge Blend Coffee</div>
  <div class="item" style="top:815px">Chai or Green Tea Latte</div>
  <div class="item" style="top:839px">Soda</div>

  <!-- Bubble tea -->
  <div class="rule" style="top:887px"></div>
  <svg class="ribbon" style="top:900px" viewBox="0 0 460 46" aria-hidden="true">
    <polygon points="0,14 40,14 40,46 0,46 12,30" fill="var(--red-dark)"/>
    <polygon points="460,14 420,14 420,46 460,46 448,30" fill="var(--red-dark)"/>
    <polygon points="28,40 40,46 40,40" fill="var(--red-fold)"/>
    <polygon points="432,40 420,46 420,40" fill="var(--red-fold)"/>
    <rect x="28" y="2" width="404" height="38" fill="var(--red)"/>
  </svg>
  <div class="ribbon-label" style="top:904px">Bubble Tea</div>
  <div class="rule" style="top:930px"></div>
  <div class="item" style="top:954px">Mango</div>
  <div class="item" style="top:978px">Honeydew</div>
  <div class="item" style="top:1002px">Blue Raspberry</div>
  <div class="item" style="top:1027px">Taro</div>
  <div class="item" style="top:1051px">Strawberry</div>
  <div class="item" style="top:1075px">Orange Cream</div>
</main>
</body>
</html>
```